Harlune Painting

Need business card design

Target Market(s)

Paint

Industry/Entity Type

Painting

Requirements
Must have
• Brice Halvorn | Superviser
| HarLune Painting
| mobile: (360) 555-0148
| email: Brice@harluneinc.example
| site: www.harluneinc.example
| address: 718 Corliss Rd NE Ste 300, Olympia, WA 98501

```html
<!DOCTYPE html>
<html lang="en">
<head>
<meta charset="utf-8">
<title>HarLune Painting – Business Card</title>
<link href="https://fonts.googleapis.com/css2?family=Montserrat:wght@400;500;600;700&display=swap" rel="stylesheet">
<style>
  :root {
    --navy: #1f3a8a;
    --blue: #2a62c4;
    --green: #5fbb46;
    --ink: #444a55;
    --card: #ffffff;
    --backdrop: #d9dbde;
  }
  * { box-sizing: border-box; margin: 0; padding: 0; }
  html, body { width: 1200px; height: 913px; overflow: hidden; }
  body {
    background: var(--backdrop);
    font-family: "Montserrat", sans-serif;
    position: relative;
  }
  .card {
    position: absolute;
    width: 620px;
    height: 354px;
    background: var(--card);
    border-radius: 16px;
    overflow: hidden;
    box-shadow: 0 6px 18px rgba(0,0,0,.18);
  }
  .card--front { left: 60px; top: 70px; }
  .card--back { left: 520px; top: 480px; }

  .wordmark {
    position: absolute;
    display: flex;
    align-items: center;
    gap: 12px;
    color: var(--navy);
    font-weight: 700;
    text-transform: uppercase;
    letter-spacing: 1px;
  }
  .wordmark__dot {
    width: 18px; height: 18px;
    border-radius: 50%;
    background: var(--green);
  }
  .card--front .wordmark {
    left: 0; right: 0; top: 150px;
    justify-content: center;
    font-size: 34px;
  }
  .card--back .wordmark {
    right: 40px; top: 62px;
    font-size: 24px;
  }

  .holder { position: absolute; left: 44px; top: 168px; }
  .holder__name {
    font-size: 26px; font-weight: 700; letter-spacing: .5px;
    text-transform: uppercase; color: var(--blue);
  }
  .holder__name span { color: var(--green); }
  .holder__role {
    font-size: 13px; color: var(--ink); letter-spacing: 1px;
    text-transform: uppercase; margin-top: 2px;
  }
  .contact { position: absolute; left: 60px; top: 236px; list-style: none; }
  .contact li {
    display: flex; align-items: center; gap: 12px;
    font-size: 15px; color: var(--ink); line-height: 26px;
  }
  .contact svg { width: 16px; height: 16px; fill: var(--navy); flex: none; }

  .divider {
    position: absolute; left: 372px; top: 186px;
    width: 2px; height: 96px; background: var(--green);
  }
  .address { position: absolute; left: 390px; top: 188px; }
  .address__company { font-size: 15px; font-weight: 700; color: var(--navy); }
  .address__company span { color: var(--green); }
  .address p { font-size: 14px; color: var(--ink); line-height: 24px; }

  .edge-line {
    position: absolute; left: 0; right: 0; bottom: 18px;
    height: 4px; background: var(--green);
  }
  .edge-band {
    position: absolute; left: 0; right: 0; bottom: 0;
    height: 14px; background: var(--navy);
  }
</style>
</head>
<body>
  <section class="card card--front">
    <div class="wordmark"><span class="wordmark__dot"></span>Harlune Painting</div>
  </section>

  <section class="card card--back">
    <div class="wordmark"><span class="wordmark__dot"></span>Harlune Painting</div>

    <div class="holder">
      <h1 class="holder__name">Brice <span>Halvorn</span></h1>
      <p class="holder__role">Superviser</p>
    </div>

    <ul class="contact">
      <li>
        <svg viewBox="0 0 24 24"><path d="M6.6 10.8a15 15 0 0 0 6.6 6.6l2.2-2.2c.3-.3.7-.4 1-.2 1.1.4 2.3.6 3.6.6.6 0 1 .4 1 1V20c0 .6-.4 1-1 1A17 17 0 0 1 3 4c0-.6.4-1 1-1h3.5c.6 0 1 .4 1 1 0 1.3.2 2.5.6 3.6.1.3 0 .7-.2 1z"/></svg>
        (360) 555-0148
      </li>
      <li>
        <svg viewBox="0 0 24 24"><path d="M2 5h20v14H2zm2 2v.5l8 5 8-5V7l-8 5z"/></svg>
        Brice@harluneinc.example
      </li>
      <li>
        <svg viewBox="0 0 24 24"><circle cx="12" cy="12" r="10"/></svg>
        www.harluneinc.example
      </li>
    </ul>

    <div class="divider"></div>
    <div class="address">
      <p class="address__company">HarLune <span>Painting</span></p>
      <p>718 Corliss Rd NE Ste 300,</p>
      <p>Olympia, WA 98501</p>
    </div>

    <div class="edge-line"></div>
    <div class="edge-band"></div>
  </section>
</body>
</html>
```